Business Card Design Project

Hello,

We have just created our new COMPANY LOGO via Fenwick Loom and would not like to turn our attention to new Business Cards.

We are a printing company based in Singapore & Las Vegas. We specialize in blue-print printing for the Architectural, Engineering and Construction industries

The design should be simple, professional, clean and organized.

The Business Cards should "pop" when seen and will hopefully be something that makes you look twice.

We have two different Pan-tones that we use for our company, feel free to use them if you think they will work for your design?

Orange: PMS 021
Gray: PMS 431

I have attached our current logo for your use and reference which should obvious be on our business cards.

Considering we have two locations on different continents, we need business cards templates where the address details need to be interchangeable for each different location (total 2)

First one:
42 Mereton Road #03-11 to #03-15
Singapore 512847
Tel : +65 6483-2207
Fax : +65 6487-9042

Second one:
3218 W. Larkspur Blvd, Suite 204
Las Vegas, Nevada 89147
Tel : (702) 555-0143
Fax : (702) 555-0178

We would also like to list a few of our key services on the card. Here are a few examples to get you going.

Plan Printing & Plotting
Digital Colour Printing
Cadline Printing
Specialty Book Making
Scanning & Archiving
Collection & Delivey

This is the first time i have requested for business cards to be created so please let me know if you require any additional information.
Many Thanks,
Tomas
Updates

Reason: It took us longer than expected to finalize our Company Logo We look forward to receiving your designs.

Target Market(s)

Our Target Market is construction related people.
Construction
Architecture
Engineering

Industry/Entity Type

Printing

Font styles to use
Other font styles liked:
• Times New Roman

Colors
faa54b
ffffff

Requirements
Must have
• The business card must have our Company Logo (attached)
The font used must be Times New Roman
Should not have
• Playful images of print designs and/or logos

```html
<!DOCTYPE html>
<html lang="en">
<head>
<meta charset="utf-8">
<title>Plancraft Print Works — Business Cards</title>
<link rel="stylesheet" href="https://fonts.googleapis.com/css2?family=Tinos:ital,wght@0,400;0,700;1,400&display=swap">
<style>
  :root {
    --orange: #faa54b;
    --orange-deep: #e8922f;
    --gray: #55595e;
    --gray-dark: #3f4347;
    --ink: #1e1e1e;
    --paper: #ffffff;
    --backdrop: #e9e9eb;
    --type: "Tinos", "Times New Roman", serif;
  }
  * { box-sizing: border-box; margin: 0; padding: 0; }
  html, body {
    width: 1200px; height: 873px; overflow: hidden;
    background: var(--backdrop);
    font-family: var(--type);
  }
  .sheet { position: relative; width: 1200px; height: 873px; }
  .card {
    position: absolute;
    width: 520px; height: 297px;
    background: var(--paper);
    overflow: hidden;
    box-shadow: 0 10px 28px rgba(0,0,0,.14);
  }
  .card-singapore { left: 50px; top: 112px; }
  .card-lasvegas { left: 630px; top: 112px; }
  .card-back { left: 340px; top: 464px; }

  .edge-band {
    position: absolute; top: 0; right: 0; bottom: 0; width: 30px;
    background: linear-gradient(90deg, var(--orange), var(--orange-deep));
  }
  .brand {
    display: flex; align-items: center; gap: 8px;
    font-weight: 700; color: var(--ink); white-space: nowrap;
  }
  .brand-mark { width: 10px; height: 10px; background: var(--ink); flex: none; }

  /* Front */
  .card-front .brand { position: absolute; top: 26px; left: 30px; font-size: 19px; }
  .name-tab {
    position: absolute; left: 0; top: 70px; width: 268px; height: 84px;
    border-radius: 0 16px 16px 0;
    background: linear-gradient(180deg, var(--orange), var(--orange-deep));
    padding: 15px 0 0 30px;
  }
  .person-name { font-size: 29px; font-weight: 700; color: var(--gray-dark); line-height: 1; }
  .person-role { margin-top: 7px; font-size: 15px; color: #6e4f2a; }
  .contact-list {
    position: absolute; left: 30px; top: 180px; list-style: none;
    font-size: 14px; color: var(--gray);
  }
  .contact-item { display: flex; gap: 9px; line-height: 20px; }
  .contact-label { display: inline-block; width: 30px; color: var(--gray-dark); font-weight: 700; }
  .contact-icon { width: 13px; height: 13px; margin-top: 4px; flex: none; fill: var(--orange-deep); }

  /* Back */
  .logo-tab {
    position: absolute; left: 0; top: 96px; width: 290px; height: 104px;
    border-radius: 0 16px 16px 0;
    background: linear-gradient(180deg, var(--orange), var(--orange-deep));
    display: flex; align-items: center; padding-left: 30px;
  }
  .card-back .brand { font-size: 22px; }
  .services {
    position: absolute; left: 316px; top: 92px; list-style: none;
    font-size: 13px; line-height: 19px; color: var(--gray);
  }
  .services-title {
    font-size: 11px; letter-spacing: .12em; text-transform: uppercase;
    color: var(--orange-deep); font-weight: 700; margin-bottom: 4px;
  }
  .service { display: flex; align-items: center; gap: 7px; }
  .service::before {
    content: ""; width: 5px; height: 5px; background: var(--orange); flex: none;
  }
  .website {
    position: absolute; top: 50%; right: 15px;
    transform: translate(50%, -50%) rotate(-90deg);
    white-space: nowrap;
    font-size: 14px; font-weight: 700;
    color: var(--gray-dark);
  }
</style>
</head>
<body>
<main class="sheet">
  <section class="card card-front card-singapore">
    <div class="brand"><span class="brand-mark"></span>Plancraft Print Works</div>
    <div class="name-tab">
      <p class="person-name">Alden Marsh</p>
      <p class="person-role">Director</p>
    </div>
    <ul class="contact-list">
      <li class="contact-item">
        <svg class="contact-icon" viewBox="0 0 16 16" aria-hidden="true"><path d="M8 1 1 8h2v7h4v-4h2v4h4V8h2z"/></svg>
        <span>42 Mereton Road #03-11 to #03-15<br>Singapore 512847</span>
      </li>
      <li class="contact-item">
        <svg class="contact-icon" viewBox="0 0 16 16" aria-hidden="true"><path d="M2 5c0-2 2-3 6-3s6 1 6 3v1h-3V5H5v1H2zM4 7h8l2 7H2zm4 2a2 2 0 1 0 0 4 2 2 0 0 0 0-4z"/></svg>
        <span><span class="contact-label">Tel</span>+65 6483-2207</span>
      </li>
      <li class="contact-item">
        <svg class="contact-icon" viewBox="0 0 16 16" aria-hidden="true"><path d="M4 1h7l2 2v4H4zM1 8h14v7H1zm2 2v1h4v-1zm0 2v1h4v-1zm8-2a1 1 0 1 0 0 2 1 1 0 0 0 0-2z"/></svg>
        <span><span class="contact-label">Fax</span>+65 6487-9042</span>
      </li>
    </ul>
    <div class="edge-band"></div>
  </section>

  <section class="card card-front card-lasvegas">
    <div class="brand"><span class="brand-mark"></span>Plancraft Print Works</div>
    <div class="name-tab">
      <p class="person-name">Alden Marsh</p>
      <p class="person-role">Director</p>
    </div>
    <ul class="contact-list">
      <li class="contact-item">
        <svg class="contact-icon" viewBox="0 0 16 16" aria-hidden="true"><path d="M8 1 1 8h2v7h4v-4h2v4h4V8h2z"/></svg>
        <span>3218 W. Larkspur Blvd, Suite 204<br>Las Vegas, Nevada 89147</span>
      </li>
      <li class="contact-item">
        <svg class="contact-icon" viewBox="0 0 16 16" aria-hidden="true"><path d="M2 5c0-2 2-3 6-3s6 1 6 3v1h-3V5H5v1H2zM4 7h8l2 7H2zm4 2a2 2 0 1 0 0 4 2 2 0 0 0 0-4z"/></svg>
        <span><span class="contact-label">Tel</span>(702) 555-0143</span>
      </li>
      <li class="contact-item">
        <svg class="contact-icon" viewBox="0 0 16 16" aria-hidden="true"><path d="M4 1h7l2 2v4H4zM1 8h14v7H1zm2 2v1h4v-1zm0 2v1h4v-1zm8-2a1 1 0 1 0 0 2 1 1 0 0 0 0-2z"/></svg>
        <span><span class="contact-label">Fax</span>(702) 555-0178</span>
      </li>
    </ul>
    <div class="edge-band"></div>
  </section>

  <section class="card card-back">
    <div class="logo-tab">
      <div class="brand"><span class="brand-mark"></span>Plancraft Print Works</div>
    </div>
    <ul class="services">
      <li class="services-title">Our Services</li>
      <li class="service">Plan Printing &amp; Plotting</li>
      <li class="service">Digital Colour Printing</li>
      <li class="service">Cadline Printing</li>
      <li class="service">Specialty Book Making</li>
      <li class="service">Scanning &amp; Archiving</li>
      <li class="service">Collection &amp; Delivery</li>
    </ul>
    <div class="edge-band"></div>
    <p class="website">www.plancraftprint.com</p>
  </section>
</main>
</body>
</html>
```